Branding Pack for new business to business cost saving site

I would like a branding pack for my new project. I would like the following designed;
a4 Presentation folder
Letterhead
Envelope
Business Card
compliment splip

We are a business cost saving site, we have access to 1000s of discount offers for daily business to business offers. I already have the logo therfore please follow th e logo for the coloutr and design.

Target Market(s)

SMEs in United Kingdom

Industry/Entity Type

Business Service

Font styles to use
Serif
Script

Colors
0255a3
fbee3d

Requirements
Must have
• The folder needs to be the same size as attached

```html
<!DOCTYPE html>
<html lang="en">
<head>
<meta charset="utf-8">
<title>Thriftmate stationery pack</title>
<link rel="stylesheet" href="https://fonts.googleapis.com/css2?family=Open+Sans:ital,wght@0,400;0,500;1,400&family=Old+Standard+TT&display=swap">
<style>
:root{
  --blue:#0a23b0;
  --navy:#08105a;
  --yellow:#fbd92e;
  --cream:#fff6cc;
  --cyan:#19b3cc;
  --silver:#c9ccd3;
  --ink:#222;
  --bg:#eceff0;
}
*{margin:0;padding:0;box-sizing:border-box}
html,body{width:1200px;height:1200px;overflow:hidden;background:var(--bg)}
body{position:relative;font-family:"Open Sans",sans-serif;color:var(--ink)}
.sheet{position:absolute;background:#fff;overflow:hidden}
.brand{font-family:"Old Standard TT",serif;font-weight:400;color:var(--blue);white-space:nowrap;line-height:1}
.brand--light{color:#fff}
.serif{font-family:"Old Standard TT",serif}
.band{position:absolute;left:0;right:0;bottom:0}
.contact{font-family:"Old Standard TT",serif;font-size:10px;line-height:14px;color:var(--ink)}
.contact-row{display:flex;gap:8px}
.contact-col{padding-right:8px;border-right:1px solid #999}
.contact-col:last-child{border:0}
.ic{display:inline-block;width:7px;height:7px;background:var(--blue);margin-right:4px;border-radius:1px}
.ic--pin{border-radius:50% 50% 50% 0;transform:rotate(-45deg)}

/* folder */
.folder{left:73px;top:68px;width:564px;height:765px}
.folder-art{position:absolute;inset:0}
.folder-copy{position:absolute;left:29px;top:480px;color:#fff;font-size:23px;line-height:33px;white-space:nowrap;text-transform:uppercase;transform:scaleX(.82);transform-origin:left top}
.folder-copy p+p{margin-top:33px}
.folder .brand{position:absolute;left:36px;top:692px;font-size:34px}

/* letterhead */
.letterhead{left:503px;top:95px;width:563px;height:763px}
.letterhead .brand{position:absolute;left:18px;top:28px;font-size:34px}
.letterhead .contact{position:absolute;left:208px;top:22px}
.letter{position:absolute;left:41px;top:138px;font-size:9.6px;line-height:19.6px;white-space:nowrap}
.letter p{margin-bottom:19.6px}
.signoff{position:absolute;left:44px;top:612px;font-size:14.5px;line-height:20px}
.signature{font-style:italic;font-size:21px;color:var(--navy);margin-top:8px;line-height:26px}

/* business cards */
.card-front{left:639px;top:285px;width:291px;height:165px}
.card-front .brand{position:absolute;left:14px;top:27px;font-size:24px}
.card-name{position:absolute;right:13px;top:77px;text-align:right}
.card-name h3{font-family:"Old Standard TT",serif;font-weight:400;font-size:13px;line-height:15px;color:var(--blue)}
.card-name span{display:block;font-size:7px;line-height:9px}
.card-rule{position:absolute;left:10px;right:14px;top:105px;border-top:1px solid #b9bde8}
.card-pin{position:absolute;left:12px;top:123px;font-size:7px;line-height:10px}
.card-lines{position:absolute;right:13px;top:113px;font-size:7px;line-height:10px;text-align:right}
.card-back{left:639px;top:503px;width:291px;height:165px;background:radial-gradient(ellipse at center,#fffdf4 0%,var(--cream) 55%,#fde79a 100%);display:flex;align-items:center;justify-content:center}
.card-back .brand{font-size:32px}

/* compliment slip */
.slip{left:34px;top:899px;width:535px;height:254px}
.slip .brand{position:absolute;left:31px;top:46px;font-size:38px}
.slip-title{position:absolute;left:279px;top:142px;font-size:16px;color:var(--blue);text-transform:uppercase}
.slip .contact{position:absolute;left:281px;top:183px;font-size:9px;line-height:12.5px}

/* envelope */
.envelope{left:597px;top:899px;width:535px;height:254px;background:linear-gradient(135deg,#fffdf5 0%,var(--cream) 60%,#fdeaa5 100%)}
.envelope .brand{position:absolute;left:23px;top:32px;font-size:38px}
.envelope .contact{position:absolute;left:24px;top:182px;font-size:14px;line-height:17px}
</style>
</head>
<body>

<section class="sheet folder">
  <svg class="folder-art" width="564" height="765" viewBox="0 0 564 765">
    <defs>
      <linearGradient id="photoTone" x1="0" y1="0" x2="1" y2="1">
        <stop offset="0" stop-color="#eceae6"/>
        <stop offset=".5" stop-color="#a9aaab"/>
        <stop offset="1" stop-color="#3b3d40"/>
      </linearGradient>
      <linearGradient id="folderBlue" x1="0" y1="0" x2="0" y2="1">
        <stop offset="0" stop-color="#1a2dbd"/>
        <stop offset="1" stop-color="#0b127a"/>
      </linearGradient>
    </defs>
    <rect width="564" height="520" fill="url(#photoTone)" role="img" aria-label="Photo of a caliper, coin stack, calculator and printed figures"/>
    <polygon points="0,208 290,372 430,378 564,470 564,490 430,398 290,392 0,228" fill="var(--cyan)"/>
    <polygon points="0,232 285,398 430,404 564,494 564,512 430,422 285,416 0,252" fill="var(--navy)"/>
    <polygon points="0,256 280,422 430,428 564,516 564,530 430,442 280,436 0,270" fill="var(--silver)"/>
    <polygon points="0,274 278,440 430,446 564,534 564,765 0,765" fill="url(#folderBlue)"/>
  </svg>
  <div class="folder-copy serif">
    <p>We are a business<br>cost saving site.....</p>
    <p>We have access to 1000s of discount<br>for daily business to business offers</p>
  </div>
  <div class="brand brand--light">Thriftmate</div>
</section>

<section class="sheet letterhead">
  <div class="brand">Thriftmate</div>
  <div class="contact contact-row">
    <div class="contact-col">
      <div><span class="ic"></span>123-456-7890</div>
      <div><span class="ic"></span>www.thriftmate.com</div>
      <div><span class="ic"></span>john@thriftmate.com</div>
    </div>
    <div class="contact-col" style="padding-top:14px">
      <div><span class="ic ic--pin"></span>Dummy city</div>
      <div style="padding-left:11px">Dummy country, land</div>
    </div>
  </div>
  <div class="letter">
    <p>To<br>The,<br>Director</p>
    <p>Lorem ipsum dolor sit amet, consectetur adipiscing elit. Integer nec odio. Praesent libero, quam a vulptate<br>dictum, massa quam dapibus leo, sed tempor nulla metus ut sagittis ipsum ligula. Pellen tesque<br>aliquam quam vel dolor cursus, sed dignissim lacus ornare, sem lacus varius ac, tellus.<br>Vestibulum ut nulla aliquam risus.</p>
    <p>Curabitur sit amet erat at nibh pharetra tempus, mauris massa mattis lacinia at, venenatis<br>non, arcu. Nunc nec tortor in quam feugiat tincidunt posuere at nibh. Curabitur<br>dolonunc,egestas at, accumsan at, malesuada nec, magna. Nulla facilisi. Nunc volutpat. Vestibulum ante<br>ipsum primis in faucibus orci luctus et ultrices posuere cubilia Curae; Ut sit amet orci vel mauris blandit<br>vehicula. Nullam quis enim. Integer dignissim viverra velit. Curabitur in odio.</p>
    <p>In hac habitasse platea dictumst. Sed ligula nisl, fringilla at momentum dolor, sed<br>imperdiet nulla tellus ut diam. Vestibulum at cerat sit amet, elit.</p>
    <p>Curabitur sit amet erat at nibh pharetra tempus, mauris massa mattis lacinia at, venenatis<br>non, arcu. Nunc nec tortor in quam feugiat tincidunt posuere at nibh. Curabitur<br>dolonunc,egestas at, accumsan at, malesuada nec, magna. Nulla facilisi. Vestibulum ante<br>ipsum primis in faucibus orci luctus et ultrices posuere sit amet orci vel mauris blandit<br>vehicula. Nullam quis enim. Integer dignissim viverra velit. Curabitur in odio..</p>
  </div>
  <div class="signoff">Thanking you,<div class="signature">John Doe</div></div>
  <svg class="band" width="563" height="20" viewBox="0 0 563 20"><polygon points="0,0 290,0 300,20 0,20" fill="var(--blue)"/><polygon points="296,0 563,0 563,20 306,20" fill="var(--yellow)"/></svg>
</section>

<section class="sheet card-front">
  <div class="brand">Thriftmate</div>
  <div class="card-name"><h3>JOHN DOE</h3><span>Director</span></div>
  <div class="card-rule"></div>
  <div class="card-pin"><span class="ic ic--pin"></span>Dummy city<br><span style="padding-left:11px">Dummy country, land</span></div>
  <div class="card-lines">123-456-7890 <span class="ic"></span><br>www.thriftmate.com <span class="ic"></span><br>john@thriftmate.com <span class="ic"></span></div>
  <svg class="band" width="291" height="12" viewBox="0 0 291 12"><polygon points="0,0 158,0 164,12 0,12" fill="var(--blue)"/><polygon points="162,0 291,0 291,12 168,12" fill="var(--yellow)"/></svg>
</section>

<section class="sheet card-back"><div class="brand">Thriftmate</div></section>

<section class="sheet slip">
  <div class="brand">Thriftmate</div>
  <div class="slip-title serif">With complements</div>
  <div class="contact contact-row">
    <div class="contact-col">
      <div><span class="ic"></span>123-456-7890</div>
      <div><span class="ic"></span>www.thriftmate.com</div>
      <div><span class="ic"></span>john@thriftmate.com</div>
    </div>
    <div class="contact-col" style="padding-top:12px">
      <div><span class="ic ic--pin"></span>Dummy city</div>
      <div style="padding-left:11px">Dummy country, land</div>
    </div>
  </div>
  <svg class="band" width="535" height="21" viewBox="0 0 535 21"><polygon points="0,0 270,0 280,21 0,21" fill="var(--blue)"/><polygon points="276,0 535,0 535,21 286,21" fill="var(--yellow)"/></svg>
</section>

<section class="sheet envelope">
  <div class="brand">Thriftmate</div>
  <div class="contact"><span class="ic ic--pin"></span>Dummy city<br><span style="padding-left:11px">Dummy country, land</span></div>
  <svg class="band" width="535" height="21" viewBox="0 0 535 21"><polygon points="0,0 270,0 280,21 0,21" fill="var(--blue)"/><polygon points="276,0 535,0 535,21 286,21" fill="var(--yellow)"/></svg>
</section>

</body>
</html>
```